Software Development Consulting Company Needs Business Card Design

We need a new business card design for our consultants at Verdant Systems (verdantsystems.example). We are a small firm that provides high-end software development and methodology consulting to medium to large enterprise IT organizations.

Our logo uses Futura for the font and we would like to stick with navy blue and canary yellow for the logo colors. Attached are normal and reversed versions of our logos in illustrator format.
Updates

Hi Everyone, Thank yo very much for your amazing design ideas. I have created a poll for this project and our employees will be voting on the design they wish to use. We will be making a decision this Wednesday (October 22nd). Thanks again, Marcus Hallward

Industry/Entity Type

Business

```html
<!DOCTYPE html>
<html lang="en">
<head>
<meta charset="utf-8">
<title>Verdant Systems — Business Card</title>
<link rel="stylesheet" href="https://fonts.googleapis.com/css2?family=Oswald:wght@300;400&display=swap">
<style>
  :root {
    --navy: #1c4a6e;
    --canary: #f5ee1a;
    --white: #ffffff;
    --ink: #060709;
    --card-font: "Oswald", "Arial Narrow", sans-serif;
  }
  * { margin: 0; padding: 0; box-sizing: border-box; }
  html, body { width: 1200px; height: 900px; overflow: hidden; background: var(--white); }
  .sheet { position: relative; width: 1200px; height: 900px; background: var(--white); font-family: var(--card-font); }
  .dark-band { position: absolute; left: 0; top: 413px; width: 1200px; height: 342px; background: var(--ink); }

  .card { position: absolute; width: 393px; height: 227px; overflow: hidden; }
  .card--navy { background: var(--navy); color: var(--white); }
  .card--light { background: var(--white); color: var(--navy); }
  .card--front-navy { left: 91px; top: 98px; }
  .card--back-navy { left: 659px; top: 98px; }
  .card--front-light { left: 91px; top: 474px; }
  .card--back-light { left: 655px; top: 474px; }

  .brand { position: absolute; left: 44px; top: 88px; display: flex; align-items: center; gap: 14px; }
  .brand__dot { width: 12px; height: 12px; border-radius: 50%; background: var(--canary); }
  .brand__name {
    font-weight: 400; font-size: 28px; letter-spacing: 5px; text-transform: uppercase; line-height: 1;
  }
  .card--navy .brand__name { color: var(--white); }
  .card--light .brand__name { color: var(--navy); }

  .contact { position: absolute; left: 34px; top: 26px; }
  .contact__name, .contact__title { font-weight: 300; font-size: 22px; line-height: 23px; margin-left: 17px; }
  .contact__title { color: var(--canary); }
  .contact__list { list-style: none; margin-top: 17px; }
  .contact__item { display: flex; align-items: center; gap: 5px; font-weight: 300; font-size: 17px; line-height: 19.5px; }
  .contact__item--accent { color: var(--canary); }
  .contact__icon { width: 12px; height: 12px; flex: none; }
  .card--navy .contact__icon { fill: var(--white); stroke: var(--white); }
  .card--light .contact__icon { fill: var(--navy); stroke: var(--navy); }
</style>
</head>
<body>
<div class="sheet">
  <div class="dark-band"></div>

  <section class="card card--navy card--front-navy">
    <div class="brand"><span class="brand__dot"></span><span class="brand__name">Verdant Systems</span></div>
  </section>

  <section class="card card--navy card--back-navy">
    <div class="contact">
      <p class="contact__name">Marcus Hallward</p>
      <p class="contact__title">Principal Consultant</p>
      <ul class="contact__list">
        <li class="contact__item"><svg class="contact__icon" viewBox="0 0 12 12"><circle cx="6" cy="6" r="5" fill="none" stroke-width="1"/><ellipse cx="6" cy="6" rx="2.2" ry="5" fill="none" stroke-width="1"/><line x1="1" y1="6" x2="11" y2="6" stroke-width="1"/></svg>marcus.hallward@verdantsystems.example</li>
        <li class="contact__item contact__item--accent"><svg class="contact__icon" viewBox="0 0 12 12"><path d="M1 4 Q6 0 11 4 L9 5.5 L8 4 H4 L3 5.5 Z M3 6 H9 L10 11 H2 Z" stroke="none"/></svg>555-014-2290</li>
        <li class="contact__item"><svg class="contact__icon" viewBox="0 0 12 12"><path d="M6 0.5 A4 4 0 0 1 10 4.5 C10 7.5 6 11.5 6 11.5 C6 11.5 2 7.5 2 4.5 A4 4 0 0 1 6 0.5 Z M6 3 A1.5 1.5 0 1 0 6 6 A1.5 1.5 0 1 0 6 3 Z" fill-rule="evenodd" stroke="none"/></svg>2240 Harbor Crest Ln, Fairview, OR 97024</li>
        <li class="contact__item contact__item--accent"><svg class="contact__icon" viewBox="0 0 12 12"><circle cx="6" cy="6" r="4.5" stroke="none"/></svg>@marcushw</li>
      </ul>
    </div>
  </section>

  <section class="card card--light card--front-light">
    <div class="brand"><span class="brand__dot"></span><span class="brand__name">Verdant Systems</span></div>
  </section>

  <section class="card card--light card--back-light">
    <div class="contact">
      <p class="contact__name">Marcus Hallward</p>
      <p class="contact__title">Principal Consultant</p>
      <ul class="contact__list">
        <li class="contact__item"><svg class="contact__icon" viewBox="0 0 12 12"><circle cx="6" cy="6" r="5" fill="none" stroke-width="1"/><ellipse cx="6" cy="6" rx="2.2" ry="5" fill="none" stroke-width="1"/><line x1="1" y1="6" x2="11" y2="6" stroke-width="1"/></svg>marcus.hallward@verdantsystems.example</li>
        <li class="contact__item contact__item--accent"><svg class="contact__icon" viewBox="0 0 12 12"><path d="M1 4 Q6 0 11 4 L9 5.5 L8 4 H4 L3 5.5 Z M3 6 H9 L10 11 H2 Z" stroke="none"/></svg>555-014-2290</li>
        <li class="contact__item"><svg class="contact__icon" viewBox="0 0 12 12"><path d="M6 0.5 A4 4 0 0 1 10 4.5 C10 7.5 6 11.5 6 11.5 C6 11.5 2 7.5 2 4.5 A4 4 0 0 1 6 0.5 Z M6 3 A1.5 1.5 0 1 0 6 6 A1.5 1.5 0 1 0 6 3 Z" fill-rule="evenodd" stroke="none"/></svg>2240 Harbor Crest Ln, Fairview, OR 97024</li>
        <li class="contact__item contact__item--accent"><svg class="contact__icon" viewBox="0 0 12 12"><circle cx="6" cy="6" r="4.5" stroke="none"/></svg>@marcushw</li>
      </ul>
    </div>
  </section>
</div>
</body>
</html>
```